Need updated stationery design for chiropractic clinic

We recently moved our office and are looking to refresh our letterhead, business cards, presentation folder and envelopes. I tend to prefer simple, clean designs. We communicate with a lot of attorneys and want to exude professionalism. I have attached our logo and 2 additional versions (all white and white letters instead of grey).

Target Market(s)

Other medical professionals and attorneys. Business cards will go to patients as well.

Industry/Entity Type

Healthcare

```html
<!DOCTYPE html>
<html lang="en">
<head>
<meta charset="utf-8">
<title>Spinewell Clinic – Business Card</title>
<link href="https://fonts.googleapis.com/css2?family=Montserrat:wght@400;600;700&display=swap" rel="stylesheet">
<style>
  :root {
    --brand-blue: #1a9acf;
    --brand-deep: #1b8fc9;
    --ink: #111111;
    --card-border: #555555;
    --tint-b: #e7eff8;
    --page: #ffffff;
  }
  * { margin: 0; padding: 0; box-sizing: border-box; }
  html, body {
    width: 1200px; height: 1000px; overflow: hidden;
    background: var(--page);
    font-family: "Montserrat", sans-serif;
  }
  .canvas { position: relative; width: 1200px; height: 1000px; }

  .card { position: absolute; left: 208px; width: 784px; height: 448px; }
  .card-front { top: 36px; background: var(--brand-blue); }
  .card-back { top: 516px; background: var(--page); border: 1px solid var(--card-border); overflow: hidden; }

  .brand-name {
    position: absolute; font-weight: 700; white-space: nowrap; line-height: 1;
  }
  .card-front .brand-name {
    left: 0; right: 0; top: 200px; text-align: center;
    color: #ffffff; font-size: 40px; letter-spacing: 0.5px;
  }
  .card-back .brand-name {
    left: 108px; top: 204px; color: var(--brand-deep); font-size: 29px;
  }

  .backdrop-tint {
    position: absolute; left: 0; top: 0; width: 376px; height: 448px;
    background: var(--tint-b); opacity: 0.55;
  }
  .brand-panel {
    position: absolute; left: 75px; top: 174px; width: 300px; height: 100px;
    background: var(--page);
  }

  .holder { position: absolute; left: 446px; top: 80px; color: var(--ink); }
  .holder-name { font-size: 24px; font-weight: 700; line-height: 1; }
  .holder-role { margin-top: 12px; font-size: 17px; font-weight: 600; line-height: 1; }

  .contact-list { position: absolute; left: 444px; top: 208px; list-style: none; }
  .contact-item {
    display: flex; align-items: center; height: 42px;
    font-size: 18px; color: var(--ink); letter-spacing: 0.2px;
  }
  .contact-icon { width: 22px; height: 22px; margin-right: 22px; flex: none; }
  .contact-icon * { fill: none; stroke: var(--brand-blue); stroke-width: 1.6; stroke-linecap: round; stroke-linejoin: round; }
</style>
</head>
<body>
<main class="canvas">
  <section class="card card-front" aria-label="Card front">
    <p class="brand-name">Spinewell Clinic</p>
  </section>

  <section class="card card-back" aria-label="Card back">
    <div class="backdrop-tint"></div>
    <div class="brand-panel"></div>
    <p class="brand-name">Spinewell Clinic</p>

    <div class="holder">
      <h1 class="holder-name">John Doe</h1>
      <p class="holder-role">Doctor</p>
    </div>

    <ul class="contact-list">
      <li class="contact-item">
        <svg class="contact-icon" viewBox="0 0 24 24" aria-hidden="true"><path d="M5 3h4l2 5-2.5 1.5a11 11 0 0 0 6 6L16 13l5 2v4a2 2 0 0 1-2 2A16 16 0 0 1 3 5a2 2 0 0 1 2-2z"/></svg>
        +44-113-496-0852
      </li>
      <li class="contact-item">
        <svg class="contact-icon" viewBox="0 0 24 24" aria-hidden="true"><rect x="3" y="6" width="18" height="12"/><path d="M3 6l9 7 9-7"/></svg>
        hello@spinewellclinic.com
      </li>
      <li class="contact-item">
        <svg class="contact-icon" viewBox="0 0 24 24" aria-hidden="true"><circle cx="12" cy="12" r="9"/><path d="M3 12h18M12 3c3 3 3 15 0 18M12 3c-3 3-3 15 0 18"/></svg>
        spinewellclinic.com
      </li>
      <li class="contact-item">
        <svg class="contact-icon" viewBox="0 0 24 24" aria-hidden="true"><path d="M12 22s7-7 7-12a7 7 0 0 0-14 0c0 5 7 12 7 12z"/><circle cx="12" cy="10" r="2.5"/></svg>
        48 Mill Road, Leeds, UK
      </li>
    </ul>
  </section>
</main>
</body>
</html>
```